Swim school needs flyer design

Need revamp of flyer design. Attached last years flyer (BCP A4 Holiday Leaflet-v6.2 (1)). Also attached is this years information in word format (BCP A4 BCP & Holiday Leaflet 2014-2015).
This flyer must fit with our logo (Blue Current Pools-RGB). This flyer is our first point of call for many of our clients. With the amount of information that must be provided, it is important that it flows and is appealing. Photos can be accessed from http://kemapics.brightfolio.net/apps/photos/album?albumid=52930417 or from your own source
Important that the final design fits printers template.(Flyers-A4-210x297mm-2Side - attached)

```html
<!DOCTYPE html>
<html lang="en">
<head>
<meta charset="utf-8">
<title>Blue Current Pools – Flyer</title>
<link rel="stylesheet" href="https://fonts.googleapis.com/css2?family=Arimo:wght@400;700&family=Roboto+Condensed:wght@400;700&display=swap">
<style>
:root{
  --green:#a6c537;
  --green-dark:#8fb02a;
  --blue:#1ba5dc;
  --teal:#157b9a;
  --orange:#f39a1f;
  --red:#e12a2d;
  --ink:#222;
  --grey:#3c3c3c;
  --paper:#fff;
  --bg:#e6e6e6;
}
*{box-sizing:border-box;margin:0;padding:0}
html,body{width:1200px;height:852px;overflow:hidden;background:var(--bg)}
body{position:relative;font-family:"Roboto Condensed",Arial,sans-serif;color:var(--ink)}
.page{position:absolute;top:70px;width:518px;height:727px;background:var(--paper);overflow:hidden;box-shadow:0 2px 8px rgba(0,0,0,.25)}
.page--terms{left:80px}
.page--holiday{left:620px}
.abs{position:absolute}
.header{position:absolute;left:0;top:0;width:518px;height:200px;background:var(--green)}
.waves{position:absolute;left:0;top:150px;width:518px;height:70px}
.title{position:absolute;right:24px;top:32px;font-family:"Arimo",Arial,sans-serif;font-weight:700;font-size:31px;color:#fff;text-align:right;text-shadow:1px 2px 3px rgba(0,0,0,.25);white-space:nowrap}
.page--holiday .title{left:36px;right:auto;text-align:left;font-size:41px;top:26px}
.subtitle{position:absolute;right:26px;top:88px;font-family:"Arimo",Arial,sans-serif;font-weight:700;font-size:20px}
.call{position:absolute;right:26px;top:120px;font-family:"Arimo",Arial,sans-serif;font-weight:700;font-size:30px;color:#fff}
.call small{font-size:22px}
.brand{position:absolute;font-family:"Roboto Condensed",Arial,sans-serif;font-weight:700;color:var(--blue);line-height:1;white-space:nowrap}
.important h3{color:var(--orange);font-size:14px;margin-bottom:6px}
.checks{list-style:none;font-size:7.4px;line-height:1.3}
.checks li{position:relative;padding-left:13px;margin-bottom:3px}
.checks li::before{content:"";position:absolute;left:0;top:1px;width:7px;height:7px;background:var(--orange);border:1px solid #b86a08}
.pathway{position:absolute;left:28px;top:250px;width:165px;height:236px;background:var(--orange);border:4px solid #fff;border-radius:22px 22px 70px 70px;color:#fff;text-align:center;padding-top:8px;z-index:3;box-shadow:0 2px 4px rgba(0,0,0,.2)}
.pathway h2{font-size:16px;line-height:1.15;margin-bottom:8px}
.pathway dt{font-weight:700;font-size:11px;color:#fff;margin-top:5px}
.pathway dd{font-size:11px;color:#fff6d8}
.photo{position:absolute;border-radius:14px;overflow:hidden}
.photo--terms{left:0;top:343px;width:498px;height:172px;background:linear-gradient(100deg,#2a8ec6,#8fc7e2 45%,#d99b86 70%,#3b87b8)}
.photo--holiday{left:30px;top:345px;width:465px;height:95px;background:linear-gradient(90deg,#3a9ec9,#f0a35a 35%,#6fbde0 65%,#6b5fa6)}
.ribbon{position:absolute;background:var(--red);color:#fff;font-size:7.5px;line-height:1.25;padding:4px 10px}
.urlbar{position:absolute;left:290px;top:493px;width:208px;height:24px;background:var(--blue);color:#fff;font-family:"Arimo",Arial,sans-serif;font-weight:700;font-size:12.5px;text-align:center;line-height:24px;z-index:2;white-space:nowrap}
.terms{position:absolute;left:18px;top:528px;display:flex;gap:8px}
.term{width:112px;height:152px;background:var(--green);border-radius:6px;padding:4px 6px;box-shadow:0 2px 3px rgba(0,0,0,.2)}
.term h4{font-family:"Arimo",Arial,sans-serif;color:#fff;font-size:17px;line-height:1.1}
.term .dates{font-weight:700;font-size:11px;line-height:1.2}
.term .book{font-size:9px;color:#fff;line-height:1.2;margin:3px 0 6px}
.term table{font-size:10px;font-weight:700;border-collapse:collapse;width:100%}
.term td{padding:1px 0}
.term td+td{text-align:right}
.note{position:absolute;left:55px;top:686px;width:410px;height:18px;background:var(--red);color:#fff;font-size:9px;text-align:center;line-height:18px}
.footband{position:absolute;left:0;bottom:0;width:518px;height:16px;background:var(--orange)}
.web{position:absolute;left:36px;top:92px;font-family:"Arimo",Arial,sans-serif;font-weight:700;font-size:20px;letter-spacing:1.4px;white-space:nowrap}
.address{position:absolute;left:36px;top:126px;font-size:10px;line-height:16px}
.dates-box{position:absolute;left:300px;top:190px;width:204px;height:156px;background:var(--orange);padding:6px 8px;z-index:2}
.dates-box h3{color:#fff;font-size:16px;text-align:center;margin-bottom:4px}
.year{background:var(--grey);border-radius:5px;padding:3px 6px;margin-bottom:4px;color:#fff}
.year b{color:var(--orange);font-size:12px}
.year ul{list-style:none;display:flex;flex-wrap:wrap;font-size:9.5px}
.year li{width:50%;padding-left:11px;position:relative;margin:1px 0}
.year li::before{content:"";position:absolute;left:0;top:2px;width:7px;height:7px;background:var(--orange)}
.pill{background:#fff;color:var(--ink);border-radius:4px;font-size:7.5px;text-align:center;padding:1px;margin:0 18px}
.headline{position:absolute;left:34px;top:452px;color:var(--teal);font-weight:700;font-size:19px}
.headline small{display:block;font-size:13px;margin-top:3px}
.info{position:absolute;left:12px;top:500px;width:240px;height:196px;background:var(--green);border-radius:8px;padding:8px 20px}
.info p{font-size:9px;line-height:1.3}
.info .lead{font-weight:700;font-size:10px}
.info h3{color:#fff;font-size:14px;margin:10px 0 5px}
.info .checks li::before{background:#fff;border-color:var(--green-dark)}
.info .checks{font-size:7.4px}
.promo{position:absolute;left:12px;top:688px;width:240px;height:34px;background:var(--red);color:#fff;font-size:7.4px;text-align:center;padding:3px 8px;line-height:1.3}
.contact{position:absolute;left:258px;top:500px;width:260px}
.contact-head{background:var(--blue);color:#fff;font-weight:700;font-size:14px;line-height:1.2;padding:4px 16px;height:48px}
.venue{background:var(--orange);margin-top:3px;padding:4px 8px 6px}
.venue h5{color:#fff;font-size:11px;font-weight:400;margin-bottom:3px}
.venue p{font-size:7.2px;line-height:1.35}
</style>
</head>
<body>

<section class="page page--terms">
  <div class="header"></div>
  <svg class="waves" viewBox="0 0 518 70" preserveAspectRatio="none" aria-hidden="true">
    <path d="M0 30 C120 0 260 45 518 10 L518 70 L0 70Z" fill="#fff"/>
    <path d="M0 25 C150 60 300 10 518 28 L518 50 C320 30 160 80 0 48Z" fill="var(--blue)"/>
    <path d="M0 48 C160 80 320 30 518 50 L518 70 L0 70Z" fill="#fff"/>
  </svg>
  <h1 class="title">Blue Current Pools Classes</h1>
  <p class="subtitle">2014/15 Term Dates &amp; Prices</p>
  <p class="call"><small>Call:</small> 94810227</p>

  <div class="brand" style="left:40px;top:205px;font-size:20px">Blue Current Pools</div>

  <div class="important abs" style="left:216px;top:200px;width:280px">
    <h3>Important</h3>
    <ul class="checks">
      <li>No bookings are taken without a fully completed enrolment form and payment.</li>
      <li>Read BCPV Policies and Procedures for information on discounts, payment methods, refunds and makeups.</li>
      <li>Book early – place are limited due to small class sizes.</li>
      <li>Bookings can only be made in person at our Kingsford Office or online.</li>
      <li>During holidays, all bookings must be done via the Kingsford Office.</li>
      <li>Photographs and video footage is not allowed to be taken without the permission of all the parents/ guardians whose children are in the class.</li>
    </ul>
  </div>

  <div class="photo photo--terms" role="img" aria-label="Photo of a parent holding a toddler in a swimming pool"></div>

  <div class="pathway">
    <h2>Our Streamlined Pathway to Success</h2>
    <dl>
      <dt>BABY AWARENESS</dt><dd>½ hour class per week</dd>
      <dt>BABY TRANSITION CLASSES</dt><dd>½ hour class per week</dd>
      <dt>BLUE CURRENT CLASSES</dt><dd>½ hour class per week</dd>
      <dt>TRANSITIONAL STROKE GROUP</dt><dd>1 hour class per week</dd>
    </dl>
  </div>

  <p class="ribbon" style="left:20px;top:490px;width:270px;z-index:4">All swimmers, male and female, are required to wear a cap – please name your cap and goggles with a biro to prevent it washing off.</p>
  <div class="urlbar">www.bluecurrentpools.com.au</div>

  <div class="terms">
    <article class="term">
      <h4>*2014:</h4>
      <p class="dates">Term 4-10 week term Oct 6th - Dec 14th</p>
      <p class="book">Bookings taken from 22nd Sep 2014</p>
      <table><tr><td>Babies</td><td>$155</td></tr><tr><td>Transition</td><td>$165</td></tr><tr><td>BCP</td><td>$170</td></tr><tr><td>TSG</td><td>$210</td></tr></table>
    </article>
    <article class="term">
      <h4>*2015:</h4>
      <p class="dates">Term 1-9 week term Jan 27th - Mar 29th</p>
      <p class="book">Bookings taken from 15th Dec 2014</p>
      <table><tr><td>Babies</td><td>$139.50</td></tr><tr><td>Transition</td><td>$148.50</td></tr><tr><td>BCP</td><td>$153</td></tr><tr><td>TSG</td><td>$189</td></tr></table>
    </article>
    <article class="term">
      <h4>*2015:</h4>
      <p class="dates">Term 2-11 week term Apr 13th - Jun 28th</p>
      <p class="book">Bookings taken from 30th Mar 2015</p>
      <table><tr><td>Babies</td><td>$170.50</td></tr><tr><td>Transition</td><td>$176</td></tr><tr><td>BCP</td><td>$181.50</td></tr><tr><td>TSG</td><td>$231</td></tr></table>
    </article>
    <article class="term">
      <h4>*2015:</h4>
      <p class="dates">Term 3-10 week term Jul 13th - Sep 20th</p>
      <p class="book">Bookings taken from 29th Jun 2015</p>
      <table><tr><td>Babies</td><td>$160</td></tr><tr><td>Transition</td><td>$170</td></tr><tr><td>BCP</td><td>$175</td></tr><tr><td>TSG</td><td>$215</td></tr></table>
    </article>
  </div>
  <p class="note">* Note that these terms have public holidays and prices will be adjusted accordingly.</p>
  <div class="footband"></div>
</section>

<section class="page page--holiday">
  <div class="header"></div>
  <svg class="waves" viewBox="0 0 518 70" preserveAspectRatio="none" aria-hidden="true">
    <path d="M0 30 C120 0 260 45 518 10 L518 70 L0 70Z" fill="#fff"/>
    <path d="M0 25 C150 60 300 10 518 28 L518 50 C320 30 160 80 0 48Z" fill="var(--blue)"/>
    <path d="M0 48 C160 80 320 30 518 50 L518 70 L0 70Z" fill="#fff"/>
  </svg>
  <h1 class="title">Holiday Swim Classes</h1>
  <p class="web">www.bluecurrentpools.com.au</p>
  <p class="address">Kingsford P.S. Pool, 42 Marlow Street Kingsford<br>Ashbury Grammar Pool, Gate 3, Dalton St Ashbury</p>

  <div class="brand" style="left:32px;top:262px;font-size:30px">Blue Current Pools</div>

  <div class="dates-box">
    <h3>Holiday Program Dates</h3>
    <div class="year"><b>2014</b>
      <ul><li>Sep 23rd - 27th</li><li>Sep 30th - Oct 4th</li></ul>
    </div>
    <div class="year"><b>2015</b>
      <ul><li>Jan 13th - 17th</li><li>Jan 20th - 24th</li><li>Mar 30th - Apr 3rd</li><li>Apr 6th - 10th</li><li>Jun 29th - Jul 3rd</li></ul>
    </div>
    <p class="pill">* $52 per child due to 4 day week</p>
  </div>

  <div class="photo photo--holiday" role="img" aria-label="Photo of children in swim caps on floats in a pool"></div>

  <p class="headline">Salt Water Pool Ages 3 and older $75 per child per week<small>(5x½ hour classes per week)</small></p>

  <div class="info">
    <p class="lead">No bookings are taken without a fully completed enrolment form and payment.</p>
    <p>Places are limited so book early to avoid disappointment.</p>
    <h3>Important</h3>
    <ul class="checks">
      <li>All holiday swim classes are conducted at the Kingsford primary school pool</li>
      <li>30 minute classes run every ½ hour from 9.30am to 12 noon</li>
      <li>Limited places due to small class sizes</li>
      <li>Beginners to advanced swimmers welcome</li>
      <li>All children are grouped by age and ability</li>
      <li>No refunds or makeups for holiday programs</li>
    </ul>
  </div>
  <p class="promo">Our qualified staff makes swimming lessons not only a rewarding but also a lot of fun. This is a great opportunity to kick-start your child's aquatic education.</p>

  <div class="contact">
    <div class="contact-head">Pool Locations Contact<br>Details &amp; Office Hours</div>
    <div class="venue">
      <h5>KINGSFORD P.S. POOL</h5>
      <p><b>Location:</b> 42 Marlow Street, Kingsford 3091 &nbsp;Phone: 9481 0227<br><b>Office Hours:</b> Mon-Fri 9:00am-5.30pm, Sat-Sun 9.15am-12.15pm</p>
    </div>
    <div class="venue">
      <h5>ASHBURY GRAMMAR POOL</h5>
      <p><b>Location:</b> Gate 3, Dalton Street, Ashbury 3093.</p>
    </div>
    <div class="venue" style="height:80px">
      <h5>ALL CORRESPONDENCE</h5>
      <p><b>Post:</b> P.O. Box 4471, East Ashbury 3093<br>Email: info@bluecurrentpools.com.au<br>ABN: 61 228 903 415</p>
    </div>
  </div>
</section>

</body>
</html>
```